Pinecrest Renovations - Get the creative juices going!!

Pinecrest does not do the actual renovation work. The company provides high end project management of renovation (primarily residential - with an eye toward commercial) The renovation work could look very different between projects. This company manages the work of contractors, architects and interior designers (either subcontracted directly by Pinecrest or hired by the client and entrusted to Pinecrest to manage). Clients are high end in the economic scale and the card needs to have a high end feel to it.

The owner is female, but the audience will be heavily slanted male. It should not be a "feminine" or "masculine" looking card. If anything, slant more on the masculine side. Clean, simple, yet creative and artistically appealing. The card design should complement and in no way compete with the logo.

When people think of our company: trust, integrity, dynamic, limitless possibilities, transition, energy, creative. We plan to expand in the future to be international.

There will also be a contest running for stationary. Please check that section, as well.

***Black is 80-90 percent black. Not stark black

Tight timeline. Needs cards printed quickly!

Residential

```html
<!DOCTYPE html>
<html lang="en">
<head>
<meta charset="utf-8">
<title>Pinecrest Renovations – Business Card</title>
<link href="https://fonts.googleapis.com/css2?family=Lato:ital,wght@0,400;0,700;1,400;1,700&display=swap" rel="stylesheet">
<style>
  :root {
    --backdrop: #4b4b4b;
    --paper: #ffffff;
    --ink: #38393b;
    --band: #434446;
    --teal: #16a69c;
    --on-dark: #ffffff;
  }
  * { box-sizing: border-box; margin: 0; padding: 0; }
  html, body {
    width: 1200px;
    height: 900px;
    overflow: hidden;
    background: var(--backdrop);
    font-family: "Lato", Arial, sans-serif;
  }
  .canvas {
    width: 1200px;
    height: 900px;
    display: flex;
    align-items: center;
    justify-content: center;
  }
  .business-card {
    width: 1000px;
    height: 572px;
    border-radius: 34px;
    overflow: hidden;
    display: flex;
    flex-direction: column;
    background: var(--paper);
  }
  .brand-area {
    height: 240px;
    display: flex;
    flex-direction: column;
    align-items: center;
    justify-content: center;
    gap: 22px;
    padding-top: 10px;
  }
  .brand-square {
    width: 58px;
    height: 58px;
    background: var(--teal);
  }
  .brand-name {
    font-size: 44px;
    font-weight: 700;
    letter-spacing: 1px;
    color: var(--ink);
    text-transform: uppercase;
  }
  .name-band {
    height: 56px;
    background: var(--band);
    color: var(--on-dark);
    display: flex;
    align-items: center;
    justify-content: center;
    gap: 8px;
  }
  .person-name {
    font-size: 32px;
    font-weight: 400;
    letter-spacing: 0.5px;
  }
  .person-title {
    font-size: 22px;
    font-weight: 400;
  }
  .contact-area {
    flex: 1;
    background: var(--teal);
    color: var(--on-dark);
    padding: 40px 72px 0;
  }
  .contact-list {
    list-style: none;
    font-size: 29px;
    line-height: 1.32;
  }
  .contact-label {
    font-style: italic;
    font-weight: 700;
  }
</style>
</head>
<body>
  <main class="canvas">
    <article class="business-card">
      <header class="brand-area">
        <div class="brand-square" aria-hidden="true"></div>
        <h1 class="brand-name">Pinecrest Renovations</h1>
      </header>
      <section class="name-band">
        <span class="person-name">YOUR NAME</span>
        <span class="person-title">-title</span>
      </section>
      <section class="contact-area">
        <ul class="contact-list">
          <li><span class="contact-label">phone</span>: 123-456-7890</li>
          <li><span class="contact-label">web</span>: yourdomain.com</li>
          <li><span class="contact-label">email</span>: yourname@yourdomain.com</li>
          <li><span class="contact-label">lic</span>: #123 456</li>
          <li><span class="contact-label">address</span>: Street address goes here, Suite #303, Alt Bldg, NY 82365</li>
        </ul>
      </section>
    </article>
  </main>
</body>
</html>
```